High-End Bifold Brochure for Aesthetics Medspa Business

I need a print-ready, bifold brochure designed for a high-end, luxurious Aesthetics/Medspa practice.

The brochure will showcase the latest IV Therapy content (6 options included in MENU.docx), and exclusive Vitamin B12+ wellness shot content (included in VB PDF). It should also include the business logo and basic office contact options.

The design should be clean, modern, and appealing with a light design. It should flow nicely and compliment the website theme/design. Preferably, having the 6 IV treatments inside bifold, with B12 shot on back/outside page. For easy viewing.

I have attached a few licensed images, if you think they will incorporate into the design nicely. Otherwise, please ignore them. If needed, I can send more.

https://velorabloomclinic.com/
Brand purple: #491c64
Fonts used on site:
Josefin Sans
Montserrat

Size should be 6.5 x 9 using specs on Quellpress's template page (Half Fold design)
https://www.quellpress.com/resources/templates

Font styles to use
Other font styles liked:
• Montserrat, Josefin Sans, or similar

Requirements
Must have
• Content included in MENU + B12 shot content on PDF.
Similar feel to the website, High-end, modern, luxurious

```html
<!DOCTYPE html>
<html lang="en">
<head>
<meta charset="utf-8">
<title>Velora Bloom Clinic – Aesthetics Medspa Brochure</title>
<link rel="stylesheet" href="https://fonts.googleapis.com/css2?family=Montserrat:wght@400;600;700;800&family=Josefin+Sans:wght@400;600&family=Open+Sans:ital,wght@0,400;0,600;1,400&display=swap">
<style>
:root{
  --stage:#ebe5e1;
  --purple:#491c64;
  --purple-deep:#2e0d45;
  --purple-bright:#6a1f8f;
  --magenta:#d12fb4;
  --orchid:#c2259f;
  --gold:#d4a941;
  --gold-light:#f0cf74;
  --paper:#ffffff;
  --ink:#2b2233;
  --muted:#5a4d63;
  --light-text:#efe3f5;
}
*{box-sizing:border-box;margin:0;padding:0}
html,body{width:1200px;height:2400px;overflow:hidden}
body{background:var(--stage);font-family:"Open Sans",sans-serif;position:relative;color:var(--ink)}
.spread{position:absolute;left:60px;width:1080px;height:748px;display:flex;box-shadow:0 18px 40px rgba(60,30,70,.18)}
.spread--outside{top:380px}
.spread--inside{top:1260px}
.page{position:relative;width:540px;height:748px;overflow:hidden}

/* back page */
.page--back{background:linear-gradient(160deg,var(--purple-bright) 0%,var(--purple) 45%,var(--purple-deep) 100%);color:var(--light-text);padding:34px 32px 0}
.back-orchid{position:absolute;right:20px;top:0;width:130px;height:60px;border-radius:0 0 40px 60px;background:radial-gradient(circle at 40% 40%,var(--magenta),var(--orchid) 60%,transparent 75%)}
.section-title{font-family:"Montserrat",sans-serif;font-weight:800;color:var(--gold);text-transform:uppercase;font-size:14px;line-height:1.15;letter-spacing:.3px}
.nutrients{display:flex;gap:22px;margin-top:12px}
.check-list{list-style:none;flex:1}
.check-list li{position:relative;padding-left:20px;font-size:8.2px;line-height:1.4;margin-bottom:7px}
.check-list li svg{position:absolute;left:0;top:1px;width:11px;height:11px}
.check-list b{color:var(--gold-light);font-weight:600}
.benefits-title{margin-top:10px}
.doctor{display:flex;gap:18px;margin-top:14px;align-items:flex-start}
.doctor-photo{width:118px;height:96px;border:3px solid var(--gold);background:linear-gradient(135deg,#c9b49a,#8c7a6c);flex:none}
.doctor-name{font-family:"Montserrat",sans-serif;font-weight:800;color:var(--gold);font-size:14px;text-transform:uppercase}
.doctor-cred{font-family:"Montserrat",sans-serif;font-size:8px;letter-spacing:1px;margin:2px 0 6px}
.doctor p,.doctor-bio{font-size:7.6px;line-height:1.45}
.doctor-bio{margin-top:10px}
.contact-bar{position:absolute;left:0;right:0;bottom:28px;height:50px;background:var(--magenta);display:flex;align-items:center;padding:0 22px;gap:16px;color:#fff}
.brand-mark{display:flex;align-items:center;gap:7px;font-family:"Montserrat",sans-serif;font-weight:600;font-size:10px;letter-spacing:.5px;text-transform:uppercase;line-height:1.1}
.brand-mark .dot{width:18px;height:18px;border-radius:50%;border:1.5px solid currentColor}
.divider{width:1px;height:30px;background:rgba(255,255,255,.7)}
.call small{display:block;font-size:8px}
.call strong{font-family:"Montserrat",sans-serif;font-size:16px;font-weight:600}
.links{font-size:8px;line-height:1.7}
.links span{display:flex;align-items:center;gap:5px}
.links svg{width:9px;height:9px}

/* cover */
.page--cover{background:linear-gradient(170deg,#5e1b82 0%,var(--purple) 50%,var(--purple-deep) 100%)}
.cover-model{position:absolute;right:0;top:0;width:260px;height:600px;background:linear-gradient(180deg,#6b4d3d 0%,#e6c2aa 18%,#f2d3bf 60%,#e9c1a8 100%);border-bottom-left-radius:120px}
.cover-orchids{position:absolute;left:110px;bottom:0;width:300px;height:240px;border-radius:140px 140px 0 0;background:radial-gradient(ellipse at 50% 60%,var(--magenta) 0%,var(--orchid) 45%,rgba(194,37,159,0) 72%)}
.cover-brand{position:absolute;left:40px;top:70px;color:#fff;font-size:14px}
.cover-brand .dot{width:26px;height:26px}
.cover-title{position:absolute;left:40px;top:140px;font-family:"Josefin Sans",sans-serif;font-weight:600;font-size:46px;line-height:1;letter-spacing:3px;color:var(--gold);text-transform:uppercase}
.cover-url{position:absolute;left:40px;top:262px;background:var(--magenta);color:#fff;font-family:"Montserrat",sans-serif;font-size:12px;font-weight:600;letter-spacing:.8px;padding:7px 14px}

/* inside */
.page--menu{background:var(--paper);padding:40px 40px 0}
.menu-head{display:flex;justify-content:space-between;align-items:flex-start}
.menu-title{font-family:"Montserrat",sans-serif;font-weight:800;color:var(--purple);font-size:20px;line-height:1.05;text-transform:uppercase}
.menu-rule{width:120px;height:3px;background:var(--gold);margin-top:6px}
.menu-head .brand-mark{color:var(--purple);font-size:8px}
.menu-list{list-style:none;margin-top:18px}
.menu-item{display:flex;justify-content:space-between;gap:18px;margin-bottom:11px}
.menu-item h3{font-family:"Montserrat",sans-serif;font-weight:700;font-size:11px;text-transform:uppercase;color:var(--ink)}
.menu-item h4{font-family:"Montserrat",sans-serif;font-weight:700;font-size:8px;text-transform:uppercase;color:var(--ink)}
.menu-item p{font-size:7.5px;font-style:italic;color:var(--muted);line-height:1.35;max-width:340px}
.price{font-family:"Montserrat",sans-serif;font-weight:700;color:var(--purple);font-size:13px;padding-top:6px}
.treatment-photo{position:absolute;left:40px;bottom:30px;width:360px;height:150px;background:linear-gradient(110deg,#3a3230 0%,#cfc3c0 45%,#efe9ea 70%,#cdb4a0 100%)}
.product-photo{position:absolute;left:400px;bottom:30px;width:100px;height:110px;background:radial-gradient(circle at 50% 55%,#d8d0a6,#b7a7c4 60%,#fff 62%)}
.page--portrait{background:linear-gradient(165deg,var(--purple) 0%,var(--purple-deep) 100%)}
.portrait-photo{position:absolute;left:50px;top:0;right:0;bottom:0;border-top-left-radius:60px;background:linear-gradient(180deg,#8c6a4a 0%,#d9b08a 25%,#efcdb3 55%,#e3b79a 100%)}
.portrait-orchids{position:absolute;right:0;bottom:0;width:260px;height:220px;background:radial-gradient(ellipse at 60% 60%,var(--magenta) 0%,var(--orchid) 45%,rgba(194,37,159,0) 72%)}
</style>
</head>
<body>

<!-- Outside: back + cover -->
<section class="spread spread--outside">
  <article class="page page--back">
    <div class="back-orchid" role="img" aria-label="Pink orchid blossom"></div>
    <h2 class="section-title">Dr. Morvell's Vitamin B12 Cocktail's<br>Essential Vitamins and Nutrients:</h2>
    <div class="nutrients">
      <ul class="check-list">
        <li><svg viewBox="0 0 12 12"><circle cx="6" cy="6" r="5.3" fill="none" stroke="#d4a941"/><path d="M3.5 6.2l1.7 1.6 3.3-3.5" fill="none" stroke="#d4a941" stroke-width="1.2"/></svg><b>Thiamine</b> – is used by the body to metabolize food for energy and maintain proper health and nerve function.</li>
        <li><svg viewBox="0 0 12 12"><circle cx="6" cy="6" r="5.3" fill="none" stroke="#d4a941"/><path d="M3.5 6.2l1.7 1.6 3.3-3.5" fill="none" stroke="#d4a941" stroke-width="1.2"/></svg><b>Riboflavin</b> – acts as an antioxidant within the body, helps protect cells from damage and supports skin and eye health.</li>
        <li><svg viewBox="0 0 12 12"><circle cx="6" cy="6" r="5.3" fill="none" stroke="#d4a941"/><path d="M3.5 6.2l1.7 1.6 3.3-3.5" fill="none" stroke="#d4a941" stroke-width="1.2"/></svg><b>Niacinamide</b> – helps maintain a healthy cardiovascular system and metabolism, brain function and healthy skin.</li>
        <li><svg viewBox="0 0 12 12"><circle cx="6" cy="6" r="5.3" fill="none" stroke="#d4a941"/><path d="M3.5 6.2l1.7 1.6 3.3-3.5" fill="none" stroke="#d4a941" stroke-width="1.2"/></svg><b>Pyridoxine</b> – is important for brain development and keeping the nervous and immune systems healthy.</li>
        <li><svg viewBox="0 0 12 12"><circle cx="6" cy="6" r="5.3" fill="none" stroke="#d4a941"/><path d="M3.5 6.2l1.7 1.6 3.3-3.5" fill="none" stroke="#d4a941" stroke-width="1.2"/></svg><b>Hydroxocobalamin</b> – helps with DNA synthesis and supports energy and the making of new proteins.</li>
      </ul>
      <ul class="check-list">
        <li><svg viewBox="0 0 12 12"><circle cx="6" cy="6" r="5.3" fill="none" stroke="#d4a941"/><path d="M3.5 6.2l1.7 1.6 3.3-3.5" fill="none" stroke="#d4a941" stroke-width="1.2"/></svg><b>Methionine</b> – aids in tissue growth and repair, as well as promoting healthy hair, skin and nails.</li>
        <li><svg viewBox="0 0 12 12"><circle cx="6" cy="6" r="5.3" fill="none" stroke="#d4a941"/><path d="M3.5 6.2l1.7 1.6 3.3-3.5" fill="none" stroke="#d4a941" stroke-width="1.2"/></svg><b>Inositol</b> – aids in the metabolic breakdown of fats and helps reduce blood cholesterol.</li>
        <li><svg viewBox="0 0 12 12"><circle cx="6" cy="6" r="5.3" fill="none" stroke="#d4a941"/><path d="M3.5 6.2l1.7 1.6 3.3-3.5" fill="none" stroke="#d4a941" stroke-width="1.2"/></svg><b>L-carnitine</b> – helps convert fatty acids into energy.</li>
        <li><svg viewBox="0 0 12 12"><circle cx="6" cy="6" r="5.3" fill="none" stroke="#d4a941"/><path d="M3.5 6.2l1.7 1.6 3.3-3.5" fill="none" stroke="#d4a941" stroke-width="1.2"/></svg><b>Chromium</b> – helps move sugar from the blood into cells, supports insulin and steady energy through the day.</li>
      </ul>
    </div>
    <h2 class="section-title benefits-title">Overall Benefits</h2>
    <div class="nutrients">
      <ul class="check-list">
        <li><svg viewBox="0 0 12 12"><circle cx="6" cy="6" r="5.3" fill="none" stroke="#d4a941"/><path d="M3.5 6.2l1.7 1.6 3.3-3.5" fill="none" stroke="#d4a941" stroke-width="1.2"/></svg>B12 helps aid in red blood cell formation and in DNA synthesis</li>
        <li><svg viewBox="0 0 12 12"><circle cx="6" cy="6" r="5.3" fill="none" stroke="#d4a941"/><path d="M3.5 6.2l1.7 1.6 3.3-3.5" fill="none" stroke="#d4a941" stroke-width="1.2"/></svg>Aids in the healthy maintenance of the immune and nervous systems</li>
        <li><svg viewBox="0 0 12 12"><circle cx="6" cy="6" r="5.3" fill="none" stroke="#d4a941"/><path d="M3.5 6.2l1.7 1.6 3.3-3.5" fill="none" stroke="#d4a941" stroke-width="1.2"/></svg>Helps improve skin tone, and strengthen nails and hair</li>
        <li><svg viewBox="0 0 12 12"><circle cx="6" cy="6" r="5.3" fill="none" stroke="#d4a941"/><path d="M3.5 6.2l1.7 1.6 3.3-3.5" fill="none" stroke="#d4a941" stroke-width="1.2"/></svg>Boosts metabolism and energy which may help reduce cravings and encourage weight loss</li>
      </ul>
      <ul class="check-list">
        <li><svg viewBox="0 0 12 12"><circle cx="6" cy="6" r="5.3" fill="none" stroke="#d4a941"/><path d="M3.5 6.2l1.7 1.6 3.3-3.5" fill="none" stroke="#d4a941" stroke-width="1.2"/></svg>Helps relieve cramping and bloating</li>
        <li><svg viewBox="0 0 12 12"><circle cx="6" cy="6" r="5.3" fill="none" stroke="#d4a941"/><path d="M3.5 6.2l1.7 1.6 3.3-3.5" fill="none" stroke="#d4a941" stroke-width="1.2"/></svg>Improves memory (which may protect against decline)</li>
        <li><svg viewBox="0 0 12 12"><circle cx="6" cy="6" r="5.3" fill="none" stroke="#d4a941"/><path d="M3.5 6.2l1.7 1.6 3.3-3.5" fill="none" stroke="#d4a941" stroke-width="1.2"/></svg>Enhances mood and lessens the effects of depression</li>
      </ul>
    </div>
    <div class="doctor">
      <div class="doctor-photo" role="img" aria-label="Portrait of the medical director in a white coat"></div>
      <div>
        <h2 class="doctor-name">Dr. Adrian Morvell</h2>
        <p class="doctor-cred">M.D., F.A.C.S.</p>
        <p>As Founder and Medical Director of Velora Bloom Clinic, Dr. Adrian Morvell has over 30 years of experience. His thorough knowledge of anatomy, refined artistry and attention to detail allow him to tailor every treatment to each patient's needs, with natural and youthful results.</p>
      </div>
    </div>
    <p class="doctor-bio">Dr. Morvell has been recognized by national physician associations and is a Fellow of the College of Surgeons. He is wholeheartedly committed to offering the highest quality care in a safe and compassionate setting, and he and his highly trained staff regularly complete continuing education in the most current approaches to patient care and customer service.</p>
    <div class="contact-bar">
      <div class="brand-mark"><span class="dot"></span>Velora Bloom<br>Clinic</div>
      <div class="divider"></div>
      <div class="call"><small>Call us now</small><strong>(555) 014-2286</strong></div>
      <div class="divider"></div>
      <div class="links">
        <span><svg viewBox="0 0 10 10"><rect x="1" y="1" width="8" height="8" rx="2.2" fill="none" stroke="#fff"/><circle cx="5" cy="5" r="1.8" fill="none" stroke="#fff"/></svg>@velorabloom</span>
        <span><svg viewBox="0 0 10 10"><circle cx="5" cy="5" r="4" fill="none" stroke="#fff"/><path d="M1 5h8M5 1c2 2.5 2 5.5 0 8M5 1c-2 2.5-2 5.5 0 8" fill="none" stroke="#fff" stroke-width=".7"/></svg>www.velorabloomclinic.com</span>
      </div>
    </div>
  </article>

  <article class="page page--cover">
    <div class="cover-model" role="img" aria-label="Close-up of a woman's face resting on her hand"></div>
    <div class="cover-orchids" role="img" aria-label="Magenta orchid flowers"></div>
    <div class="brand-mark cover-brand"><span class="dot"></span>Velora Bloom<br>Clinic</div>
    <h1 class="cover-title">Aesthetics<br>Medspa</h1>
    <p class="cover-url">www.velorabloomclinic.com</p>
  </article>
</section>

<!-- Inside: IV menu + portrait -->
<section class="spread spread--inside">
  <article class="page page--menu">
    <header class="menu-head">
      <div>
        <h2 class="menu-title">The Drip Lounge<br>IV Therapy</h2>
        <div class="menu-rule"></div>
      </div>
      <div class="brand-mark"><span class="dot"></span>Velora Bloom<br>Clinic</div>
    </header>
    <ul class="menu-list">
      <li class="menu-item"><div><h3>Immunity Booster</h3><p>Have a cold, flu or just need to give your immunity a boost? Let us mix a powerful punch in our booster bag just for you to prevent or relieve aches and pain.</p></div><span class="price">$150</span></li>
      <li class="menu-item"><div><h3>Refresh &amp; Hydrate</h3><p>Relieve dehydration from the extremes of lifestyle with our balanced electrolyte cocktail targeting jet lag.</p></div><span class="price">$100</span></li>
      <li class="menu-item"><div><h3>Migraine Buster</h3><p>Eradicate your migraine pain, nausea, vomiting, and light sensitivity with our magic formula.</p></div><span class="price">$150</span></li>
      <li class="menu-item"><div><h3>Wellness Infusion</h3><h4>Myer's Cocktail</h4><p>This infusion of vitamins, minerals and electrolytes results in direct access of these nutrients into your cells, enhancing energy, decreasing stress and anxiety in addition to improving memory.</p></div><span class="price">$180</span></li>
      <li class="menu-item"><div><h3>GLO</h3><p>A beauty mixture of Glutathione, Biotin and our special formula created to strengthen your hair, nails and skin for that special look!</p></div><span class="price">$200</span></li>
      <li class="menu-item"><div><h3>The Ultimate Weight Loss Infusion</h3><p>Our unique fat burning formula targets fatty deposits resulting in a more defined and contoured appearance.</p></div><span class="price">$200</span></li>
      <li class="menu-item"><div><h3>NAD+ IV: The Fountain of Youth (+-)</h3><p>Anti-aging co-enzyme NAD+ in conjunction with vitamins elevates brain health and beauty, all in one IV treatment!</p></div><span class="price">$350</span></li>
    </ul>
    <div class="treatment-photo" role="img" aria-label="Physician performing a facial treatment on a patient"></div>
    <div class="product-photo" role="img" aria-label="Skincare product with flowers"></div>
  </article>

  <article class="page page--portrait">
    <div class="portrait-photo" role="img" aria-label="Portrait of a woman with long hair wearing glasses"></div>
    <div class="portrait-orchids" role="img" aria-label="Magenta orchid flowers"></div>
  </article>
</section>

</body>
</html>
```